Business card design needed

Family General Practitioner/ Family Physician.
Logo is the logo of the Crestmoor Guild of Family Clinicians Australia
http://kvplm.tarevo.edu.au/PictureGallery/logos/pages/CGFC%20logo_jpg.htm

Reason: Just a bit more time to make changes and the weekend for me to look at things closely and to choose. Thanks, Lumi

Thanks for all the submissions. So many of them are really works of art. Not one of them are not good. The ones that I am eliminating are the ones that I think are not suitable for me personally only, and because if I don't, it makes it very difficult to decide as many of you are also sending me slight variations of a card. I have just decided to choose a second place card too. Can't thank you all enough. Good luck, Lumi. P.S - Working today till 10 pm as the card says :-), so probably won't be able to give a feedback till late Saturday night or Sunday morning here in Sydney, Australia. 

Reason: Just added a second place to the budget and realised that Australia is ahead of the rest of the world in the time zone (only :-) - don't want to offend anyone or start a debate!! ) , so Monday deadline will mean it will be a weekend for the rest of the world. Just wanted to give everyone more time to submit their best, especially since I will be picking a second card too. Can't thank everyone enough for the submissions. P.S - Not keen on photos on the card.

Contact Information for Business Card

Dr. Lumi Harcourt M.B.B.S., F.C.G.F.C
Family General Practitioner
Address, timings, phone and fax number on the back.

Requirements
Must have
• Timings
Mon 7 am - 7 pm
Tues 7 am - 12 pm
Wed 7 am - 10 pm
Thurs 7 am - 12 pm
Fri 7 am - 8 pm
Sat 8 am - 10 pm
Sun - Off

```html
<!DOCTYPE html>
<html lang="en">
<head>
<meta charset="utf-8">
<title>Dr. Lumi Harcourt – Business Card</title>
<link rel="stylesheet" href="https://fonts.googleapis.com/css2?family=Bodoni+Moda:ital,wght@1,700;1,800&family=EB+Garamond:ital,wght@1,500;1,600&display=swap">
<style>
  :root {
    --page: #ffffff;
    --stone-light: #9fb3c9;
    --stone-mid: #8aa0b9;
    --stone-dark: #7890ab;
    --band: rgba(255, 255, 255, 0.28);
    --ink-light: #ffffff;
    --ink-dark: #111418;
    --display: "Bodoni Moda", "Didot", serif;
    --book: "EB Garamond", "Garamond", serif;
  }
  * { margin: 0; padding: 0; box-sizing: border-box; }
  html, body { width: 972px; height: 1200px; overflow: hidden; background: var(--page); }
  .canvas { position: relative; width: 972px; height: 1200px; }

  .card {
    position: absolute; left: 104px; width: 765px; height: 472px; overflow: hidden;
  }
  .card--front { top: 51px; }
  .card--back { top: 583px; }

  .stone-texture {
    position: absolute; inset: 0;
    background: linear-gradient(135deg, var(--stone-light) 0%, var(--stone-mid) 50%, var(--stone-dark) 100%);
  }
  .lower-band { position: absolute; left: 0; right: 0; bottom: 0; background: var(--band); }
  .card--front .lower-band { top: 337px; }
  .card--back .lower-band { top: 310px; }

  .card p { position: absolute; white-space: nowrap; }
  .light { color: var(--ink-light); text-shadow: 1px 1px 2px rgba(30, 45, 70, 0.45); }

  .title-line {
    left: 0; right: 0; text-align: center;
    font-family: var(--display); font-style: italic; font-weight: 700;
    font-size: 40px; letter-spacing: 0.28em; line-height: 1;
  }
  .title-line--family { top: 20px; padding-right: 20px; }
  .title-line--general { top: 73px; padding-right: 30px; }
  .title-line--practitioner { top: 125px; padding-left: 30px; }

  .doctor-name, .qualifications {
    font-family: var(--book); font-style: italic; font-weight: 600;
    font-size: 37px; letter-spacing: -0.04em; line-height: 48px; text-align: center;
    transform: translateX(-50%); top: 226px;
  }
  .doctor-name { left: 162px; }
  .qualifications { left: 612px; }

  .guild-mark {
    position: absolute; display: flex; flex-direction: column; align-items: center; gap: 8px;
    transform: translate(-50%, -50%);
    font-family: var(--display); font-style: italic; font-weight: 700; font-size: 26px;
    color: var(--ink-light); letter-spacing: 0.06em;
  }
  .guild-mark__circle { width: 46px; height: 46px; border-radius: 50%; background: var(--ink-light); opacity: 0.85; }
  .guild-mark--front { left: 376px; top: 247px; }
  .guild-mark--back-left { left: 120px; top: 155px; }
  .guild-mark--back-right { left: 639px; top: 155px; }

  .welcome {
    left: 115px; width: 508px; top: 12px; text-align: justify; text-align-last: justify;
    font-family: var(--display); font-style: italic; font-weight: 800; font-size: 40px; line-height: 1;
  }

  .hours {
    position: absolute; left: 233px; top: 62px; width: 300px;
    font-family: var(--display); font-style: italic; font-weight: 700; font-size: 25px;
    border-collapse: collapse; color: var(--ink-light); text-shadow: 1px 1px 2px rgba(30, 45, 70, 0.45);
  }
  .hours td { height: 33px; padding: 0; line-height: 33px; }
  .hours .day { width: 110px; }
  .hours .time { text-align: center; }

  .address, .contact {
    font-family: var(--book); font-style: italic; font-weight: 500; color: var(--ink-dark);
  }
  .address--street { left: 18px; top: 318px; font-size: 27px; letter-spacing: -0.02em; }
  .address--suburb { left: 0; right: 0; top: 366px; text-align: center; font-size: 27px; padding-right: 30px; }
  .contact { top: 411px; font-size: 35px; }
  .contact--phone { left: 18px; }
  .contact--fax { left: 412px; }
</style>
</head>
<body>
<main class="canvas">

  <section class="card card--front" aria-label="Card front">
    <div class="stone-texture" role="img" aria-label="Blue-grey flagstone texture background"></div>
    <div class="lower-band"></div>
    <p class="title-line title-line--family light">Family</p>
    <p class="title-line title-line--general light">General</p>
    <p class="title-line title-line--practitioner light">Practitioner</p>
    <p class="doctor-name light">Doctor<br>Lumi Harcourt</p>
    <div class="guild-mark guild-mark--front"><span class="guild-mark__circle"></span>CGFC</div>
    <p class="qualifications light">M.B.B.S.<br>F.C.G.F.C</p>
  </section>

  <section class="card card--back" aria-label="Card back">
    <div class="stone-texture" role="img" aria-label="Blue-grey flagstone texture background"></div>
    <div class="lower-band"></div>
    <p class="welcome light">WELCOME</p>
    <div class="guild-mark guild-mark--back-left"><span class="guild-mark__circle"></span>CGFC</div>
    <table class="hours">
      <tr><td class="day">Mon.</td><td class="time">7 am - 7 pm</td></tr>
      <tr><td class="day">Tues.</td><td class="time">7 am - 12 pm</td></tr>
      <tr><td class="day">Wed.</td><td class="time">7 am - 10 pm</td></tr>
      <tr><td class="day">Thurs.</td><td class="time">7 am - 12 pm</td></tr>
      <tr><td class="day">Fri.</td><td class="time">7 am - 8 pm</td></tr>
      <tr><td class="day">Sat.</td><td class="time">8 am - 10 pm</td></tr>
      <tr><td class="day">Sun.</td><td class="time">Closed</td></tr>
    </table>
    <div class="guild-mark guild-mark--back-right"><span class="guild-mark__circle"></span>CGFC</div>
    <p class="address address--street">Upper Level Garden Court, Bellridge Tower Shopping Centre</p>
    <p class="address address--suburb">Bellridge, NSW 2199</p>
    <p class="contact contact--phone">Phone: 02 5550 1400</p>
    <p class="contact contact--fax">Fax: 02 5550 1233</p>
  </section>

</main>
</body>
</html>
```